I want a business card that is going to show a creative spark but without limiting me to an industry. Something edgy but that wont go out of date. I want it state My business name Verity Lanes, profession - Professional Makeup Artist contact number and email

My service is to provide makeup services from bridal, fashion, photography, film, TV and so on. It is creative and different so i want that to be reflected.

I would like the card double sided.
Updates

 I would LOVE a background on my card something like this image... i can supply an image to be formed like this

Please use the image uploaded

Can we try using the image provided on one side of the card and then writing and details on the other side

Target Market(s)

I am targeting a wide range of people from Creative directors to the individual eg. bride

Industry/Entity Type

Business

Requirements
Must have
• Name: Harriet Cole
contact numbe 0417 583 940
email address:info@veritylanes.example
website: www.veritylanes.example
One of the images attached

professional makeup artist / hair stylist

I want it to show creativity
Nice to have
• logo, Double-sided card
Should not have
• the design should not use tradional style. Or images that are not my own

```html
<!DOCTYPE html>
<html lang="en">
<head>
<meta charset="utf-8">
<title>Verity Lanes – Business Card</title>
<link rel="stylesheet" href="https://fonts.googleapis.com/css2?family=Jost:wght@400;500&family=Open+Sans:wght@400&display=swap">
<style>
  :root {
    --crimson-top: #ea2150;
    --crimson-bottom: #cf0030;
    --crimson: #e01f4b;
    --ink: #181818;
    --paper: #ffffff;
    --stage-top: #ffffff;
    --stage-bottom: #c6c6c6;
    --label: #111111;
    --shadow: rgba(0, 0, 0, 0.75);
  }
  * { margin: 0; padding: 0; box-sizing: border-box; }
  html, body { width: 1200px; height: 588px; overflow: hidden; }
  body {
    position: relative;
    background: linear-gradient(to bottom, var(--stage-top) 0%, var(--stage-bottom) 100%);
    font-family: "Jost", "Futura", sans-serif;
  }
  .side-label {
    position: absolute;
    top: 58px;
    font-family: "Open Sans", "Myriad Pro", sans-serif;
    font-size: 32px;
    letter-spacing: 1px;
    color: var(--label);
  }
  .side-label--front { left: 46px; }
  .side-label--back { left: 653px; }

  .card {
    position: absolute;
    top: 152px;
    width: 500px;
    height: 285px;
    overflow: hidden;
    box-shadow: 10px 14px 10px var(--shadow);
  }
  .card--front { left: 46px; }
  .card--back { left: 653px; }

  .band { position: absolute; left: 0; width: 100%; }
  .band--crimson { background: linear-gradient(to bottom, var(--crimson-top), var(--crimson-bottom)); }
  .band--ink { background: var(--ink); }

  .wordmark {
    display: flex;
    align-items: center;
    gap: 8px;
    font-weight: 400;
    font-size: 24px;
    letter-spacing: 0.5px;
    color: var(--paper);
    line-height: 1;
    white-space: nowrap;
  }
  .wordmark__dot {
    width: 14px;
    height: 14px;
    border-radius: 50%;
    background: var(--crimson);
  }

  /* Front */
  .front__top { top: 0; height: 97px; }
  .front__middle { top: 97px; height: 88px; }
  .front__bottom { top: 185px; height: 100px; }
  .front__identity {
    position: absolute;
    top: 122px;
    left: 0;
    width: 100%;
    display: flex;
    flex-direction: column;
    align-items: center;
    gap: 6px;
  }
  .tagline {
    font-size: 9px;
    letter-spacing: 1.6px;
    line-height: 12px;
    color: var(--paper);
  }

  /* Back */
  .back__top { top: 0; height: 37px; }
  .back__middle { top: 37px; height: 206px; }
  .back__bottom { top: 243px; height: 42px; }
  .back__wordmark { position: absolute; left: 34px; top: 71px; }
  .contact-list {
    position: absolute;
    left: 58px;
    top: 109px;
    list-style: none;
  }
  .contact-list li {
    font-size: 9px;
    letter-spacing: 1.6px;
    color: var(--paper);
    line-height: 24px;
    white-space: nowrap;
  }
  .portrait-slot {
    position: absolute;
    right: 0;
    top: 53px;
    width: 45px;
    height: 150px;
    background: linear-gradient(to right, rgba(224, 31, 75, 0) 0%, rgba(224, 31, 75, 0.35) 100%);
  }
  .services {
    position: absolute;
    left: 0;
    top: 243px;
    width: 100%;
    height: 30px;
    display: flex;
    justify-content: center;
    align-items: center;
    gap: 24px;
    list-style: none;
    padding-left: 6px;
  }
  .services li {
    font-size: 9px;
    letter-spacing: 1.6px;
    color: var(--paper);
  }
</style>
</head>
<body>
  <p class="side-label side-label--front">Front :</p>
  <p class="side-label side-label--back">Back :</p>

  <section class="card card--front" aria-label="Card front">
    <div class="band band--crimson front__top"></div>
    <div class="band band--ink front__middle"></div>
    <div class="band band--crimson front__bottom"></div>
    <div class="front__identity">
      <div class="wordmark"><span class="wordmark__dot"></span>VERITY LANES</div>
      <p class="tagline">Professional Makeup Artist</p>
    </div>
  </section>

  <section class="card card--back" aria-label="Card back">
    <div class="band band--crimson back__top"></div>
    <div class="band band--ink back__middle"></div>
    <div class="band band--crimson back__bottom"></div>
    <div class="wordmark back__wordmark"><span class="wordmark__dot"></span>VERITY LANES</div>
    <ul class="contact-list">
      <li>Harriet Cole – Professional Makeup Artist</li>
      <li>Phone : 0417 583 940</li>
      <li>E-mail : info@veritylanes.example</li>
      <li>Web : www.veritylanes.example</li>
    </ul>
    <div class="portrait-slot" role="img" aria-label="Line drawing of a woman with flowing hair in crimson strokes"></div>
    <ul class="services">
      <li>Bridal</li>
      <li>Fashion</li>
      <li>Photography</li>
      <li>Film</li>
      <li>TV</li>
    </ul>
  </section>
</body>
</html>
```